Redesign our company's business card. HSG BUSINESS CARD 2015

We are an Audio Visual Production company with a flare of marketing and sales. Lights camera ACTION!! We are Production and creative designers and thinkers whom provide first class service for many vantage 300 companies that Exhibit at trade shows and sales meetings.

Double sided, sleek, fashionable, and modern.

www.halvernstudio.com

Think ZNQ'S Crestline

Target Market(s)

Trade Show Mangers, Event coordinators, Project managers,

Industry/Entity Type

Marketing

Contact Information for Business Card

Name Tile, Logo, Slogan, photos of our work on the back. Chatterly and blipper

Font styles to use
Sans Serif
Decorative
Script

Colors
33a6d7
ffffff
0692cd
cee9f5

Requirements
Must have
• Multi color, professional, Upscale,
• CREATING GREAT PARTNERSHIPS THAT PRODUCE AMAZING RESULTS
Nice to have
• Photos of our work on the back
Should not have
• Address or fax.

```html
<!DOCTYPE html>
<html lang="en">
<head>
<meta charset="utf-8">
<title>HSG Business Card</title>
<link rel="stylesheet" href="https://fonts.googleapis.com/css2?family=Orbitron:wght@500;700&family=Rajdhani:wght@500;600&display=swap">
<style>
  :root {
    --backdrop: #e6e9ec;
    --card: #ffffff;
    --card-shade: #eef0f2;
    --frame: #a9b0b6;
    --blue: #0692cd;
    --blue-light: #33a6d7;
    --blue-pale: #cee9f5;
    --ink: #2b2f33;
  }
  * { box-sizing: border-box; margin: 0; padding: 0; }
  html, body { width: 1200px; height: 897px; overflow: hidden; }
  body {
    background: var(--backdrop);
    font-family: "Rajdhani", sans-serif;
    color: var(--ink);
    position: relative;
  }
  .card {
    position: absolute;
    top: 283px;
    width: 540px;
    height: 330px;
    border-radius: 26px;
    background: linear-gradient(160deg, var(--card) 55%, var(--card-shade));
    box-shadow: 0 10px 28px rgba(0,0,0,.18);
    overflow: hidden;
  }
  .card-front { left: 45px; }
  .card-back { left: 615px; }
  .card-frame {
    position: absolute;
    inset: 16px;
    border: 2.5px solid var(--frame);
    border-radius: 16px;
  }
  .accent-band {
    position: absolute;
    left: 0;
    top: 150px;
    width: 250px;
    height: 40px;
    border-radius: 0 20px 20px 0;
    background: linear-gradient(180deg, var(--blue-pale), var(--blue-light) 45%, var(--blue));
    border: 2px solid #2a86b0;
    border-left: none;
  }
  .accent-tab {
    position: absolute;
    right: 40px;
    bottom: 0;
    width: 40px;
    height: 78px;
    border-radius: 14px 14px 0 0;
    background: linear-gradient(90deg, var(--blue), var(--blue-light) 50%, var(--blue));
  }
  .identity {
    position: absolute;
    left: 44px;
    top: 46px;
  }
  .person-name {
    font-family: "Orbitron", sans-serif;
    font-weight: 700;
    font-size: 19px;
    letter-spacing: 1px;
  }
  .person-title {
    font-family: "Orbitron", sans-serif;
    font-weight: 500;
    font-size: 11px;
    letter-spacing: 1.5px;
    margin-top: 4px;
  }
  .brand {
    display: flex;
    align-items: center;
    gap: 12px;
  }
  .card-front .brand { position: absolute; right: 60px; top: 124px; }
  .brand-dot {
    width: 40px; height: 40px; border-radius: 50%;
    background: var(--blue);
  }
  .brand-name {
    font-family: "Orbitron", sans-serif;
    font-weight: 700;
    font-size: 40px;
    line-height: 1;
    color: var(--blue);
    letter-spacing: 3px;
  }
  .back-content {
    position: absolute;
    inset: 16px;
    display: flex;
    flex-direction: column;
    align-items: center;
    justify-content: center;
    gap: 22px;
  }
  .card-back .brand-dot { width: 52px; height: 52px; }
  .card-back .brand-name { font-size: 52px; }
  .slogan {
    font-family: "Orbitron", sans-serif;
    font-weight: 500;
    font-size: 9.5px;
    letter-spacing: 1.2px;
    color: var(--ink);
    text-align: center;
    white-space: nowrap;
  }
  .contacts {
    position: absolute;
    left: 44px;
    top: 212px;
    list-style: none;
    font-size: 13px;
    font-weight: 600;
    line-height: 20px;
  }
  .contacts li { display: flex; align-items: center; gap: 8px; }
  .contacts svg { width: 11px; height: 11px; fill: var(--ink); flex: none; }
</style>
</head>
<body>
  <section class="card card-front" aria-label="Business card front">
    <div class="card-frame"></div>
    <div class="accent-band"></div>
    <div class="accent-tab"></div>
    <div class="identity">
      <p class="person-name">DARREN VOSS</p>
      <p class="person-title">GENERAL MANAGER</p>
    </div>
    <div class="brand">
      <span class="brand-dot"></span>
      <span class="brand-name">HSG</span>
    </div>
    <ul class="contacts">
      <li><svg viewBox="0 0 12 12"><path d="M2 1l2 0 1 3-1.5 1a6 6 0 0 0 3.5 3.5L8 7l3 1v2a1 1 0 0 1-1 1A9 9 0 0 1 1 2a1 1 0 0 1 1-1z"/></svg>014 552 7310</li>
      <li><svg viewBox="0 0 12 12"><rect x="3" y="0.5" width="6" height="11" rx="1" fill="none" stroke="#2b2f33" stroke-width="1.3"/></svg>014 552 7310</li>
      <li><svg viewBox="0 0 12 12"><path d="M1 3h10v7H1z M1 3l5 4 5-4" fill="none" stroke="#2b2f33" stroke-width="1.3"/></svg>hello@halvernstudio.com</li>
      <li><svg viewBox="0 0 12 12"><circle cx="6" cy="6" r="5"/></svg>www.halvernstudio.com</li>
    </ul>
  </section>

  <section class="card card-back" aria-label="Business card back">
    <div class="card-frame"></div>
    <div class="back-content">
      <div class="brand">
        <span class="brand-dot"></span>
        <span class="brand-name">HSG</span>
      </div>
      <p class="slogan">CREATING GREAT PARTNERSHIPS THAT PRODUCE AMAZING RESULTS</p>
    </div>
  </section>
</body>
</html>
```